Female Focused - Finance Company needs a website

I need a website for a new company based in London called 'Lorinda Pelham Associates'. The company has been set up with a focus on empowering creativity and encouraging women to engage with finance and build their knowledge and understanding. I am targeting professional women and entrepreneurs in the late 20s to 40s age bracket. The mission is to empower women to achieve financial independence and inspire community and connectivity. I want to create a brand that promotes financial security, growth and connectivity.

The website at this stage can be relatively simple, I just want to be able to have a section about me and the work that I do, have contact details for people to be able to get in touch and find out more.

I run a series of different events and want to have a page whereby I can showcase the events that I am running. They can also use links to click through and register for events. I also want to be able to put images up of previous events that I have run. Maybe having a calendar on the website of different things that are happening.

I am creating a membership club called Hop3Hop and I want to have a page whereby they can find out about the membership and the different options that are available.

I have attached the logo below so you can see the designs so far.

I also own the domain name lorindapelhamassociates.com

```html
<!DOCTYPE html>
<html lang="en">
<head>
<meta charset="utf-8">
<title>Lorinda Pelham Associates</title>
<link href="https://fonts.googleapis.com/css2?family=Playfair+Display:wght@400;500&family=Roboto:wght@400;500;700&display=swap" rel="stylesheet">
<style>
:root{
  --blue:#0d62b3;
  --blue-dark:#0a4f95;
  --orange:#ef7a22;
  --ink:#222;
  --grey:#777;
  --soft:#f3f3f3;
  --white:#fff;
}
*{box-sizing:border-box;margin:0;padding:0}
html,body{width:1200px;height:3873px;overflow:hidden}
body{font-family:'Roboto',sans-serif;color:var(--ink);background:var(--white);position:relative}
.serif{font-family:'Playfair Display',serif}
section,header,footer{position:relative;width:1200px}
.abs{position:absolute}
.btn{position:absolute;display:flex;align-items:center;justify-content:center;border-radius:30px;background:var(--orange);color:#fff;font-weight:700;font-size:14px;box-shadow:0 6px 14px rgba(0,0,0,.15)}
.rule{position:absolute;height:3px;background:var(--blue)}
.photo{position:absolute}

/* header */
.site-header{height:120px}
.topbar{position:absolute;top:0;right:0;width:624px;height:36px;background:var(--blue);clip-path:polygon(0 0,100% 0,100% 100%,36px 100%);color:#fff;font-size:13px;display:flex;align-items:center;gap:14px;padding-left:70px}
.topbar .dot{width:22px;height:22px;border:1.5px solid #fff;border-radius:50%;display:inline-block}
.brand{position:absolute;left:112px;top:14px;display:flex;align-items:center;gap:8px}
.brand .ring{width:60px;height:60px;border:2px solid var(--ink);border-radius:50%}
.brand span{font-family:'Playfair Display',serif;font-size:14px;line-height:1.2;width:80px;color:var(--ink)}
.nav{position:absolute;top:72px;left:391px;display:flex;gap:32px;font-size:14px;font-weight:500}
.nav .active{color:var(--blue)}

/* hero */
.hero{height:605px;background:linear-gradient(90deg,#eef0f2 0%,#e6e3de 45%,#c8b49e 75%,#d9cfc4 100%)}
.hero h1{position:absolute;left:112px;top:100px;font-size:40px;font-weight:400;line-height:48px;color:var(--blue)}
.hero p{position:absolute;left:112px;top:213px;width:470px;font-size:18px;line-height:28px;color:#2a2a2a}

/* about */
.about{height:648px}
.about h2{position:absolute;left:112px;top:118px;font-size:48px;font-weight:400}
.about p{position:absolute;left:112px;top:215px;width:450px;font-size:14.5px;line-height:26.5px;color:var(--grey);text-align:justify}

/* why */
.why{height:490px;background:var(--soft);text-align:center}
.sec-title{position:absolute;left:0;width:1200px;text-align:center;font-family:'Playfair Display',serif;font-size:33px;font-weight:400}
.feature{position:absolute;top:155px;width:300px;text-align:center}
.feature .icon{width:104px;height:104px;margin:0 auto;border-radius:50%;background:#fff;box-shadow:0 6px 14px rgba(0,0,0,.12);display:flex;align-items:center;justify-content:center}
.feature h3{margin-top:34px;font-size:17px;font-weight:500}
.feature .bar{width:36px;height:3px;background:var(--blue);margin:10px auto 18px}
.feature p{font-size:13.5px;line-height:24px;color:var(--grey)}

/* events */
.events{height:702px;background:linear-gradient(120deg,#0a4c92,#0d62b3 50%,#0a4f9a)}
.event{position:absolute;top:170px;width:307px;height:360px}
.event .frame{position:absolute;left:0;top:0;width:307px;height:222px;border:3px solid #fff}
.event .box{position:absolute;left:0;top:187px;width:287px;height:170px;background:#fff;padding:20px 16px}
.event .date{font-size:13px;color:var(--orange)}
.event h4{margin-top:10px;font-size:17px;font-weight:500;line-height:26px}
.event p{margin-top:10px;font-size:13.5px;line-height:22px;color:var(--grey);text-align:justify}

/* gallery */
.gallery{height:570px}
.tile{position:absolute;top:187px;width:228px;height:251px;background:#fff;padding:4px;box-shadow:0 4px 12px rgba(0,0,0,.15)}
.tile .photo{left:4px;top:4px;width:220px;height:243px}
.tile .label{position:absolute;left:24px;top:225px;width:180px;height:54px;border-radius:30px;background:#fff;box-shadow:0 4px 12px rgba(0,0,0,.15);display:flex;align-items:center;justify-content:center;font-size:15px;font-weight:500}

/* membership */
.member{height:355px;background:linear-gradient(90deg,#e96e1f,#ef7a22 50%,#e56c1c);color:#fff;text-align:center}
.member p{position:absolute;left:125px;top:145px;width:950px;font-size:14.5px;line-height:26px;font-weight:500}

/* footer */
.site-footer{height:383px}
.site-footer h5{position:absolute;top:78px;font-size:17px;font-weight:500}
.links{position:absolute;left:336px;top:120px;list-style:none;font-size:14px}
.links li{height:38.5px;display:flex;align-items:flex-start;gap:16px}
.links li::before{content:"";width:11px;height:11px;border-radius:50%;background:var(--blue);margin-top:3px}
.contact{position:absolute;left:533px;top:120px;font-size:11.5px;line-height:20px;color:#444}
.contact b{display:block;font-size:13.5px;font-weight:500;color:var(--ink)}
.contact div{position:relative;padding-left:34px;margin-bottom:14px}
.contact svg{position:absolute;left:0;top:3px}
.signup{position:absolute;left:778px;top:118px;width:310px;height:44px;border-radius:25px;box-shadow:0 4px 12px rgba(0,0,0,.12);font-size:13px;color:#666;padding:13px 18px}
.signup .go{position:absolute;right:4px;top:4px;width:103px;height:36px;border-radius:20px;background:var(--orange);color:#fff;font-weight:700;font-size:12px;display:flex;align-items:center;justify-content:center}
.socials{position:absolute;left:778px;top:190px;display:flex;gap:8px}
.socials span{width:32px;height:32px;border-radius:50%;border:1px solid #ccc}
.socials span:first-child{background:var(--orange);border-color:var(--orange)}
.copyright{position:absolute;left:112px;top:332px;width:976px;border-top:1px solid #ddd;padding-top:20px;text-align:center;font-size:13px;color:#444}
</style>
</head>
<body>

<header class="site-header">
  <div class="topbar"><span>&#9742; +1 (555) 010 0199</span><span>|</span><span>&#9993; info@LPAssociates.com</span><span style="margin-left:16px;display:flex;gap:4px"><i class="dot"></i><i class="dot"></i><i class="dot"></i></span></div>
  <div class="brand"><div class="ring"></div><span>Lorinda Pelham Associates</span></div>
  <nav class="nav"><span class="active">HOME</span><span>ABOUT ME</span><span>SERVICES</span><span>EVENTS</span><span>GALLERY</span><span>CONTACT</span></nav>
  <div class="btn" style="left:952px;top:57px;width:136px;height:46px">GET A QUOTE</div>
</header>

<section class="hero">
  <div class="photo" role="img" aria-label="Woman in a striped shirt working on a laptop at a bright office desk" style="left:560px;top:0;width:640px;height:605px;background:linear-gradient(90deg,rgba(230,226,220,0),rgba(190,170,148,.6))"></div>
  <h1 class="serif">LORINDA PELHAM<br>ASSOCIATES</h1>
  <p>The mission is to empower women to achieve financial independence and inspire community and connectivity. I want to create a brand that promotes financial security, growth and connectivity.</p>
  <div class="btn" style="left:112px;top:350px;width:136px;height:45px">GET A QUOTE</div>
  <svg class="abs" style="left:0;top:0" width="1200" height="605" viewBox="0 0 1200 605">
    <path d="M0 440 Q600 760 1200 435 L1200 605 L0 605Z" fill="#fff"/>
    <path d="M90 487 Q600 740 1115 480 Q600 705 90 487Z" fill="var(--orange)"/>
  </svg>
</section>

<section class="about">
  <h2 class="serif">ABOUT ME</h2>
  <div class="rule" style="left:112px;top:175px;width:83px"></div>
  <p>Sed ut perspiciatis unde omnis iste natus error sit voluptatem accusantium doloremque laudantium, totam rem aperiam, eaque ipsa quae ab illo inventore veritatis et quasi architecto beatae vitae dicta sunt explicabo. Nemo enim ipsam voluptatem quia voluptas sit aspernatur aut odit aut fugit, sed quia consequuntur magni dolores eos qui ratione voluptatem sequi nescue porro quisquam est qui dolore.</p>
  <div class="btn" style="left:112px;top:435px;width:142px;height:48px">READ MORE</div>
  <svg class="abs" style="left:610px;top:50px" width="480" height="480" viewBox="0 0 480 480">
    <circle cx="240" cy="240" r="237" fill="var(--blue)"/>
    <circle cx="218" cy="254" r="222" fill="#dfe7ee"/>
  </svg>
  <div class="photo" role="img" aria-label="Woman doing accounts with a calculator beside a computer in a bright office" style="left:620px;top:80px;width:420px;height:440px;border-radius:50%;background:radial-gradient(circle at 60% 40%,#f4f6f8,#c9d5df)"></div>
  <div class="abs" style="left:615px;top:370px;width:150px;height:150px;border-radius:50%;background:#fff;box-shadow:0 6px 16px rgba(0,0,0,.15);display:flex;align-items:center;justify-content:center;text-align:center;font-family:'Playfair Display',serif;font-size:13px;line-height:16px">Lorinda<br>Pelham<br>Associates</div>
</section>

<section class="why">
  <div class="sec-title" style="top:60px">WHY LORINDA PELHAM ASSOCIATES</div>
  <div class="rule" style="left:559px;top:110px;width:83px"></div>
  <div class="feature" style="left:108px"><div class="icon"><svg width="52" height="52" viewBox="0 0 52 52" fill="none" stroke="var(--orange)" stroke-width="2"><path d="M6 46h40M10 40V30M18 40V24M26 40V20M34 40V14M42 40V10M8 26 L20 16 L28 20 L44 6"/></svg></div><h3>LORUM IPSUM DOL</h3><div class="bar"></div><p>Lorem ipsum dolor sit amet, consectetur adipiscing elit, sed do eiusmod tempor incididunt ut laborea.</p></div>
  <div class="feature" style="left:450px"><div class="icon"><svg width="52" height="52" viewBox="0 0 52 52" fill="none" stroke="var(--orange)" stroke-width="2"><circle cx="26" cy="18" r="10"/><path d="M6 38 L18 30 L30 36 L46 28 M10 46 L26 42 L42 46"/></svg></div><h3>LORUM IPSUM DOL</h3><div class="bar"></div><p>Lorem ipsum dolor sit amet, consectetur adipiscing elit, sed do eiusmod tempor incididunt ut laborea.</p></div>
  <div class="feature" style="left:792px"><div class="icon"><svg width="52" height="52" viewBox="0 0 52 52" fill="none" stroke="var(--orange)" stroke-width="2"><rect x="8" y="8" width="36" height="26" rx="2"/><path d="M4 40h44M20 14h12M20 20h12"/><rect x="30" y="24" width="12" height="10"/></svg></div><h3>LORUM IPSUM DOL</h3><div class="bar"></div><p>Lorem ipsum dolor sit amet, consectetur adipiscing elit, sed do eiusmod tempor incididunt ut laborea.</p></div>
</section>

<section class="events">
  <div class="sec-title" style="top:68px;color:#fff">LATEST EVENTS</div>
  <div class="rule" style="left:559px;top:118px;width:83px;background:#fff"></div>
  <div class="event" style="left:112px"><div class="frame photo" role="img" aria-label="Woman smiling in a business meeting" style="background:linear-gradient(135deg,#c9d3dc,#6f8497)"></div><div class="box"><div class="date">07 Jul 2022</div><h4>Lorem ipsum dolor sit ame consectetur adipea</h4><p>Sed ut perspiciatis unde omnis iste natus err tatem accusea...</p></div></div>
  <div class="event" style="left:446px"><div class="frame photo" role="img" aria-label="Woman working on a laptop by a window" style="background:linear-gradient(135deg,#e8ecef,#9aa7b1)"></div><div class="box"><div class="date">07 Jul 2022</div><h4>Lorem ipsum dolor sit ame consectetur adipea</h4><p>Sed ut perspiciatis unde omnis iste natus err tatem accusea...</p></div></div>
  <div class="event" style="left:780px"><div class="frame photo" role="img" aria-label="Woman reviewing finances on a laptop in a kitchen" style="background:linear-gradient(135deg,#d9dcdf,#7d8790)"></div><div class="box"><div class="date">07 Jul 2022</div><h4>Lorem ipsum dolor sit ame consectetur adipea</h4><p>Sed ut perspiciatis unde omnis iste natus err tatem accusea...</p></div></div>
  <div class="btn" style="left:520px;top:574px;width:159px;height:47px">REGISTER NOW</div>
</section>

<section class="gallery">
  <div class="sec-title" style="top:88px">GALLERY</div>
  <div class="rule" style="left:572px;top:140px;width:56px"></div>
  <div class="tile" style="left:113px"><div class="photo" role="img" aria-label="Portrait of a businesswoman" style="background:linear-gradient(#e9e4dc,#b7a898)"></div><div class="label">LORUM IPSUM</div></div>
  <div class="tile" style="left:362px"><div class="photo" role="img" aria-label="Stacks of coins with financial chart" style="background:linear-gradient(#a6c4e3,#1f4f86)"></div><div class="label">LORUM IPSUM</div></div>
  <div class="tile" style="left:611px"><div class="photo" role="img" aria-label="Woman thinking at a laptop" style="background:linear-gradient(#6a6f6b,#2e3431)"></div><div class="label">LORUM IPSUM</div></div>
  <div class="tile" style="left:859px"><div class="photo" role="img" aria-label="Women meeting in a modern office" style="background:linear-gradient(#cfd8d5,#5a6a66)"></div><div class="label">LORUM IPSUM</div></div>
</section>

<section class="member">
  <div class="sec-title" style="top:72px;color:#fff">JOIN OUR MEMBERSHIP CLUB</div>
  <p>Sed ut perspiciatis unde omnis iste natus error sit voluptatem accusantium doloremque laudantium, totam rem aperiam, eaque ipsa quae ab illo inventore veritatis et quasi architecto beatae vitae dicta sunt explicabo. Nemo enim ipsam voluptatem quia voluptas sit aspernatur aut odit aut fugit, sed quia consequuntur magni dolores eos qui ratione.</p>
  <div class="btn" style="left:540px;top:248px;width:120px;height:45px;background:var(--blue)">HOP3HOP</div>
</section>

<footer class="site-footer">
  <div class="abs" style="left:112px;top:100px;width:148px;height:150px;display:flex;flex-direction:column;align-items:center;justify-content:center;gap:10px"><div style="width:90px;height:90px;border:2px solid var(--ink);border-radius:50%"></div><span class="serif" style="font-size:14px;text-align:center">Lorinda Pelham Associates</span></div>
  <h5 style="left:336px">QUICK LINKS</h5>
  <ul class="links"><li>Home</li><li>About Me</li><li>Services</li><li>Events</li><li>Gallery</li></ul>
  <h5 style="left:533px">CONTACT INFO</h5>
  <div class="contact">
    <div><svg width="12" height="14" viewBox="0 0 12 14"><path d="M6 0a5 5 0 0 1 5 5c0 4-5 9-5 9S1 9 1 5a5 5 0 0 1 5-5z" fill="var(--blue)"/></svg><b>ADDRESS:</b>465, Lorum Ipsum Dolore,<br>London</div>
    <div><svg width="14" height="14" viewBox="0 0 14 14"><path d="M3 1l3 3-2 2c1 2 2 3 4 4l2-2 3 3-2 2C6 13 1 8 1 3z" fill="var(--blue)"/></svg><b>PHONE:</b>+1 (555) 010 0199</div>
    <div><svg width="14" height="11" viewBox="0 0 14 11"><rect width="14" height="11" fill="var(--blue)"/><path d="M0 0l7 6 7-6" stroke="#fff" fill="none"/></svg><b>EMAIL:</b>info@LPAssociates.com</div>
  </div>
  <h5 style="left:778px">NEWSLETTER SIGNUP</h5>
  <div class="signup">Email Address<div class="go">SIGN UP</div></div>
  <div class="socials" aria-label="Social links"><span></span><span></span><span></span></div>
  <div class="copyright">© 2023 Lorinda Pelham Associates &nbsp;-&nbsp; All Rights Reserved</div>
</footer>

</body>
</html>
```